Tech Laundry service company looking for a new modern and clean web site

Our site is www.brisklinenhub.com we are looking to rebrand our whole website.

We offer free pickup and delivery for laundry and dry cleaning in the NYC area. we target residential customers.

Sites to compare are www.trypolvex.com and www.zentumo.com
Most content can be found at www.brisklinenhub.com

We are looking for a clean and modern look. Nothing to busy

colors and font we use are
Logo font: Harabara
Slogan font: Swiss 721 Light Extended BT

Dark blue: C 100 M 88 Y 0 K 0
Light blue: C 85 M 50 Y 0 K 0
Orange: C 0 M 80 Y 95 K 0

Violet: C 85 M 100 Y 0 K 0

We use only Marlo, Quilse and vendrax
We are provide eco-friendly
next day laundry service

Our mission Statement is to deliver the Cleanest and Brightest clothes in the market. we use only top of the line

"We are the #1 proud supporter of Marlo and Quilse"

There will be 4 pages
the home page
and a 2 page scheduling page

THE HOME PAGE-
navigation bar must include

Home,
Clean my Clothes (schedule a pickup)
Pricing
Blog
Service Area
Commercial/Wholesale
Sign in
must have key elements about our business such as:
1. Our Price is 1.10 a lb
2. "New customers get 50% off first order and 100% off second order!"
3. we have next day service on all laundry orders
Again, you can pull the content off our current website brisklinenhub.com

Order Page-

Attached please find 5 steps of the ordering page. We are looking to condense into 2
we want step2+step3+step4 on one page
then step1+step5 on the second page on step5 we want the coinbird logo attached as well (as we do all credit card processing through CoinBird)
at the end of the process we want to offer them to create a password to auto register
the order confirmation is attached as well. we need all that info but would like it to seem cleaner and modern.

PRICING PAGE-

Wash and Fold 1.10 per Lb ($27 min charge)
Blankets $12 and up
Bathroom Rugs $5.00 and up

Dry Cleaning
Launder and Press shirt 1.25
Suit Jacket 6.00
Pants and Skirts 6.00
2 pc suit 12.00
Dress 10.00 and up
Blouses & Sweaters 6.00

Again, we are looking for a clean and sleek site not to busy.

Based on this we will be needed another 6-8 pages of design work that will be negotiated with the winner at the end of this contest.
Good Luck!

Target Market(s)

our customers are between the ages of 22-40 years old all live in NYC

Industry/Entity Type

Dry Cleaning

Number of Pages Required

4 page

Font styles to use
Other font styles liked:
• Harabara

Requirements
Must have
• sleek and cool design
• see www.polvex.com and zentumo.com for concept
• Our current site is brisklinenhub.com which we are looking to rebrand
Nice to have
• colors and font we use are
• Logo font: Harabara
• Slogan font: Swiss 721 Light Extended BT
• Dark blue: C 100 M 88 Y 0 K 0
• Light blue: C 85 M 50 Y 0 K 0
• Orange: C 0 M 80 Y 95 K 0
• Violet: C 85 M 100 Y 0 K 0
Should not have
• we want all the colors to be uniform. we are sending a message that we are the brightest and cleanest laundry service in the city!

```html
<!DOCTYPE html>
<html lang="en">
<head>
<meta charset="utf-8">
<title>Washvane.com – Fresh Folds, Next Day</title>
<link href="https://fonts.googleapis.com/css2?family=Open+Sans:ital,wght@0,300;0,400;0,600;0,700;1,400;1,600&display=swap" rel="stylesheet">
<style>
:root{
  --blue:#1a7bc9;
  --blue-dark:#1565a8;
  --orange:#f15a24;
  --ink:#2d2d2d;
  --muted:#666;
  --soft:#f2f2f2;
  --line:#dcdcdc;
  --white:#fff;
}
*{margin:0;padding:0;box-sizing:border-box}
html,body{width:1200px;height:3000px;overflow:hidden}
body{font-family:"Open Sans",Arial,sans-serif;color:var(--ink);background:var(--white);position:relative}
section,header,footer{position:absolute;left:0;width:1200px}
.abs{position:absolute}

/* header */
.site-header{top:0;height:125px;background:var(--white)}
.brand{left:40px;top:22px}
.brand-name{font-size:38px;font-weight:700;color:var(--blue);letter-spacing:-1px;line-height:1}
.brand-tag{font-size:13px;color:var(--muted);letter-spacing:1px;margin-top:4px}
.main-nav{right:40px;top:48px;display:flex;gap:30px;align-items:center}
.main-nav a{font-size:13px;color:var(--blue);text-decoration:none;text-transform:uppercase}
.main-nav .sign-in{background:var(--orange);color:var(--white);padding:5px 12px;font-weight:600}

/* hero */
.hero{top:125px;height:540px;background:linear-gradient(110deg,#d9dde0 0%,#f4f4f4 45%,#e9ecee 100%)}
.hero-photo{left:0;top:0;width:1200px;height:540px}
.hero-panel{left:155px;top:5px;width:340px;height:535px;background:var(--blue);color:var(--white);text-align:center;padding-top:30px}
.hero-title{font-size:19px;font-weight:600;line-height:1.5}
.checklist{list-style:none;text-align:left;margin:26px 0 0 40px}
.checklist li{font-size:16px;height:40px;display:flex;align-items:center;gap:20px}
.hero-book{font-size:14px;font-weight:700;margin-top:34px}
.btn-primary{display:inline-block;background:var(--orange);color:var(--white);font-size:15px;padding:10px 30px;margin-top:22px;text-transform:uppercase}
.hero-or{font-size:11px;margin-top:10px}
.hero-call{font-size:21px;font-weight:600;margin-top:4px}
.slider-arrow{top:250px;width:26px;height:44px;background:var(--blue);display:flex;align-items:center;justify-content:center}

/* partner strip */
.partners{top:665px;height:120px;background:var(--soft);display:flex;justify-content:space-around;align-items:center;padding:0 80px}
.partner-mark{width:46px;height:46px;background:#bdbdbd;border-radius:50%}
.partner-mark.wide{width:120px;height:22px;border-radius:3px}

/* process */
.process{top:785px;height:430px;background:var(--blue);color:var(--white);text-align:center}
.process-title{top:62px;width:1200px;font-size:27px;font-weight:300}
.step{top:175px;width:260px;margin-left:-130px}
.step-icon{width:110px;height:110px;margin:0 auto}
.step-name{font-size:20px;margin-top:28px}
.step-text{font-size:14px;line-height:1.5;margin-top:6px;opacity:.92}
.step-highlight{font-size:19px;line-height:1.2;margin-top:22px}

/* quality */
.quality{top:1215px;height:425px}
.quality-photo{left:0;top:0;width:1200px;height:425px;background:linear-gradient(120deg,#c8cdd2 0%,#e2e4e6 40%,#9b6b45 85%,#7a5133 100%)}
.quality-card{left:190px;top:40px;width:835px;height:345px;background:var(--white);box-shadow:0 4px 14px rgba(0,0,0,.25);text-align:center;padding:40px 60px 0}
.quality-title{font-size:22px;font-weight:400}
.quality-body{font-size:14px;line-height:1.55;color:#444;margin-top:16px}
.quality-note{font-size:15px;font-style:italic;font-weight:600;margin-top:16px;color:#555}
.features{display:flex;justify-content:space-around;margin-top:36px}
.feature{width:200px;font-size:14px;line-height:1.4;color:#444}
.feature svg{display:block;margin:0 auto 8px}

/* testimonials */
.testimonials{top:1640px;height:350px;background:var(--soft)}
.testimonial{top:48px;width:260px;margin-left:-130px;text-align:center}
.avatar{width:94px;height:94px;border-radius:50%;margin:0 auto;border:4px solid var(--white);box-shadow:0 0 0 1px var(--line);background:radial-gradient(circle at 50% 40%,#d9c2ae 0%,#9aa3ab 70%)}
.quote{font-size:14.5px;line-height:1.45;color:#444;margin-top:22px}
.cite{font-size:14px;font-weight:600;margin-top:14px}

/* trust */
.trust{top:1990px;height:355px;background:var(--white)}
.trust-title{top:58px;width:1200px;text-align:center;font-size:22px;font-weight:400}
.trust-item{top:148px;width:300px}
.trust-head{display:flex;align-items:center;gap:14px;font-size:18px}
.trust-text{font-size:13px;line-height:1.55;color:#555;margin:18px 0 0 58px}
.readmore{font-size:11px;margin:26px 0 0 58px;color:#333}

/* app */
.app{top:2345px;height:280px;background:var(--soft);text-align:center}
.app-icon{margin:40px auto 0;display:block}
.app-title{font-size:37px;font-weight:600;margin-top:12px;letter-spacing:.5px}
.app-sub{font-size:14px;font-weight:600;margin-top:6px}
.stores{display:flex;justify-content:center;gap:10px;margin-top:16px}
.store-badge{width:78px;height:26px;background:#111;border-radius:4px}

/* footer */
.site-footer{top:2625px;height:335px;background:var(--blue);color:var(--white)}
.foot-brand{left:118px;top:62px;text-align:center}
.foot-brand .brand-name{color:var(--white);font-size:32px}
.foot-brand .brand-tag{color:var(--white);font-size:12px;margin-top:8px}
.social{left:122px;top:168px;display:flex;gap:22px}
.social span{font-size:13px;font-weight:600}
.foot-col{top:55px}
.foot-heading{font-size:14px;text-transform:uppercase;margin-bottom:14px}
.foot-links{list-style:none}
.foot-links li{font-size:14px;line-height:26px}
.qa-text{font-size:13.5px;line-height:1.75;width:320px}
.seal{width:66px;height:30px;background:#e8e8e8;margin-top:20px}
.cards{display:flex;gap:6px;margin-top:10px}
.card-chip{width:48px;height:22px;background:var(--white);color:var(--blue-dark);font-size:10px;font-weight:600;display:flex;align-items:center;justify-content:center}
.copyright{left:0;top:2960px;width:1200px;height:40px;text-align:right;padding:14px 40px 0 0;font-size:12px}
</style>
</head>
<body>

<header class="site-header">
  <div class="brand abs">
    <div class="brand-name">Washvane.com</div>
    <div class="brand-tag">Fresh Folds, Next Day</div>
  </div>
  <nav class="main-nav abs">
    <a href="#">Home</a>
    <a href="#">Schedule a Pickup</a>
    <a href="#">Pricing</a>
    <a href="#">Blog</a>
    <a href="#">Service Area</a>
    <a href="#">Commercial</a>
    <a href="#" class="sign-in">Sign In</a>
  </nav>
</header>

<section class="hero">
  <div class="hero-photo abs" role="img" aria-label="Smiling laundry attendant in a white uniform folding a white shirt in a bright laundromat with washing machines"></div>
  <div class="slider-arrow abs" style="left:0"><svg width="12" height="16" viewBox="0 0 12 16"><path d="M9 2 3 8l6 6" fill="none" stroke="#fff" stroke-width="2.5"/></svg></div>
  <div class="slider-arrow abs" style="right:0"><svg width="12" height="16" viewBox="0 0 12 16"><path d="M3 2l6 6-6 6" fill="none" stroke="#fff" stroke-width="2.5"/></svg></div>
  <div class="hero-panel abs">
    <h1 class="hero-title">Top Notch Laundry Service<br>for Apartments &amp; Condos</h1>
    <ul class="checklist">
      <li><svg width="16" height="16" viewBox="0 0 16 16"><rect x="1" y="1" width="14" height="14" fill="none" stroke="#fff" stroke-width="1.5"/><path d="M4 8l3 3 5-6" fill="none" stroke="#fff" stroke-width="1.8"/></svg>Cash free Payment</li>
      <li><svg width="16" height="16" viewBox="0 0 16 16"><rect x="1" y="1" width="14" height="14" fill="none" stroke="#fff" stroke-width="1.5"/><path d="M4 8l3 3 5-6" fill="none" stroke="#fff" stroke-width="1.8"/></svg>Saves your time</li>
      <li><svg width="16" height="16" viewBox="0 0 16 16"><rect x="1" y="1" width="14" height="14" fill="none" stroke="#fff" stroke-width="1.5"/><path d="M4 8l3 3 5-6" fill="none" stroke="#fff" stroke-width="1.8"/></svg>Safety First</li>
      <li><svg width="16" height="16" viewBox="0 0 16 16"><rect x="1" y="1" width="14" height="14" fill="none" stroke="#fff" stroke-width="1.5"/><path d="M4 8l3 3 5-6" fill="none" stroke="#fff" stroke-width="1.8"/></svg>Easy to get help</li>
      <li><svg width="16" height="16" viewBox="0 0 16 16"><rect x="1" y="1" width="14" height="14" fill="none" stroke="#fff" stroke-width="1.5"/><path d="M4 8l3 3 5-6" fill="none" stroke="#fff" stroke-width="1.8"/></svg>Cash free Payment</li>
    </ul>
    <div class="hero-book">BOOK A TRUSTED LAUNDRY IN 2 MINUTES</div>
    <a class="btn-primary">Schedule a Pickup</a>
    <div class="hero-or">OR</div>
    <div class="hero-call">Call us: 212 555-0148</div>
  </div>
</section>

<section class="partners" aria-label="Featured partners">
  <div class="partner-mark"></div>
  <div class="partner-mark wide"></div>
  <div class="partner-mark wide" style="width:80px;height:30px"></div>
  <div class="partner-mark"></div>
  <div class="partner-mark" style="border-radius:6px"></div>
  <div class="partner-mark"></div>
</section>

<section class="process">
  <h2 class="process-title abs">Pick a date and time, Pay Online, and RELAX</h2>
  <div class="step abs" style="left:150px">
    <svg class="step-icon" viewBox="0 0 110 110"><rect x="22" y="22" width="66" height="66" transform="rotate(45 55 55)" fill="none" stroke="rgba(255,255,255,.7)" stroke-width="1.5"/><rect x="42" y="44" width="26" height="22" fill="none" stroke="#fff" stroke-width="1.6"/><path d="M42 50h26M48 40v7M62 40v7" stroke="#fff" stroke-width="1.6"/></svg>
    <div class="step-name">Book</div>
    <div class="step-text">You can call or schedule a<br>pickup online</div>
  </div>
  <div class="step abs" style="left:450px">
    <svg class="step-icon" viewBox="0 0 110 110"><rect x="22" y="22" width="66" height="66" transform="rotate(45 55 55)" fill="none" stroke="rgba(255,255,255,.7)" stroke-width="1.5"/><path d="M39 46h20v16H39zM59 51h8l4 5v6H59" fill="none" stroke="#fff" stroke-width="1.6"/><circle cx="45" cy="64" r="3" fill="#fff"/><circle cx="65" cy="64" r="3" fill="#fff"/></svg>
    <div class="step-name">Pick Up</div>
    <div class="step-text">we'll pick it up on the same day.<br>Free pickup and deliver</div>
  </div>
  <div class="step abs" style="left:750px">
    <svg class="step-icon" viewBox="0 0 110 110"><rect x="22" y="22" width="66" height="66" transform="rotate(45 55 55)" fill="none" stroke="rgba(255,255,255,.7)" stroke-width="1.5"/><circle cx="50" cy="42" r="4" fill="none" stroke="#fff" stroke-width="1.6"/><path d="M50 47v12l-5 9M50 59l5 9M44 52h12M58 56h8v10h-8z" fill="none" stroke="#fff" stroke-width="1.6"/></svg>
    <div class="step-name">Deliver</div>
    <div class="step-text">we have next day service on all<br>laundry orders</div>
  </div>
  <div class="step abs" style="left:1050px">
    <svg class="step-icon" viewBox="0 0 110 110"><rect x="22" y="22" width="66" height="66" transform="rotate(45 55 55)" fill="none" stroke="rgba(255,255,255,.7)" stroke-width="1.5"/><circle cx="55" cy="55" r="13" fill="none" stroke="#fff" stroke-width="1.6"/><circle cx="50" cy="52" r="1.6" fill="#fff"/><circle cx="60" cy="52" r="1.6" fill="#fff"/><path d="M49 58q6 6 12 0" fill="none" stroke="#fff" stroke-width="1.6"/></svg>
    <div class="step-highlight">You relax<br>while we take<br>care of your<br>Laundry needs</div>
  </div>
</section>

<section class="quality">
  <div class="quality-photo abs" role="img" aria-label="Close view of an open front-loading washing machine door in a laundry room"></div>
  <div class="quality-card abs">
    <h2 class="quality-title">Quality Service at Low Prices. Imagine That.</h2>
    <p class="quality-body">The Brisk Linen Hub is NYC Laundry Delivery service at its best. Founded in 2008, our business has expanded to six locations and serves all of Manhattan! We offer free laundry delivery service for a set price of $1.10 per pound for residential and commercial customers.</p>
    <p class="quality-note">We also offer dry-cleaning services at great prices.</p>
    <div class="features">
      <div class="feature"><svg width="26" height="26" viewBox="0 0 26 26"><circle cx="13" cy="13" r="11" fill="none" stroke="#888" stroke-width="1.3"/><path d="M8 13l3.5 3.5L18 10" fill="none" stroke="#888" stroke-width="1.6"/></svg>Next Day Delivery<br>laundry service</div>
      <div class="feature"><svg width="26" height="26" viewBox="0 0 26 26"><circle cx="13" cy="13" r="11" fill="none" stroke="#888" stroke-width="1.3"/><path d="M8 13l3.5 3.5L18 10" fill="none" stroke="#888" stroke-width="1.6"/></svg>We use only Marlo,<br>Quilse and vendrax</div>
      <div class="feature"><svg width="26" height="26" viewBox="0 0 26 26"><circle cx="13" cy="13" r="11" fill="none" stroke="#888" stroke-width="1.3"/><path d="M8 13l3.5 3.5L18 10" fill="none" stroke="#888" stroke-width="1.6"/></svg>We are provide<br>eco-friendly</div>
    </div>
  </div>
</section>

<section class="testimonials">
  <div class="testimonial abs" style="left:220px">
    <div class="avatar" role="img" aria-label="Portrait of a smiling customer"></div>
    <p class="quote">"The detergent that you<br>guys use smells so good!,<br>I've gotten complements<br>on the smell!"</p>
    <p class="cite">Marisol - Manhattan</p>
  </div>
  <div class="testimonial abs" style="left:600px">
    <div class="avatar" role="img" aria-label="Portrait of a smiling customer"></div>
    <p class="quote">"The detergent that you<br>guys use smells so good!,<br>I've gotten complements<br>on the smell!"</p>
    <p class="cite">Marisol - Manhattan</p>
  </div>
  <div class="testimonial abs" style="left:980px">
    <div class="avatar" role="img" aria-label="Portrait of a smiling customer"></div>
    <p class="quote">"The detergent that you<br>guys use smells so good!,<br>I've gotten complements<br>on the smell!"</p>
    <p class="cite">Marisol - Manhattan</p>
  </div>
</section>

<section class="trust">
  <h2 class="trust-title abs">Your Trust and Security are Our Priority</h2>
  <div class="trust-item abs" style="left:60px">
    <div class="trust-head"><svg width="40" height="32" viewBox="0 0 40 32"><circle cx="15" cy="9" r="6" fill="var(--blue)"/><path d="M3 28q0-11 12-11t12 11z" fill="var(--blue)"/><circle cx="29" cy="11" r="4" fill="var(--blue)"/><path d="M26 19q11-1 11 9h-8" fill="var(--blue)"/></svg>Customer Recommended</div>
    <p class="trust-text">Edce euismod consequat ante.<br>Lorem ipsum dolor sit amet,<br>consectetuer adipiscing elit.<br>Pellentesque sed dolor.</p>
    <p class="readmore">Readmore</p>
  </div>
  <div class="trust-item abs" style="left:440px">
    <div class="trust-head"><svg width="40" height="32" viewBox="0 0 40 32"><circle cx="20" cy="16" r="13" fill="none" stroke="var(--blue)" stroke-width="2.2"/><circle cx="15" cy="13" r="2" fill="var(--blue)"/><circle cx="25" cy="13" r="2" fill="var(--blue)"/><path d="M13 19q7 7 14 0" fill="none" stroke="var(--blue)" stroke-width="2.2"/></svg>Complete Peace of Mind</div>
    <p class="trust-text">Every piece of laundry is handle<br>with care by our trained atten-<br>dants, we guarantee our ser-<br>vice by double checking you</p>
    <p class="readmore">Readmore</p>
  </div>
  <div class="trust-item abs" style="left:835px">
    <div class="trust-head"><svg width="40" height="32" viewBox="0 0 40 32"><path d="M20 2l12 4v9q0 11-12 15Q8 26 8 15V6z" fill="none" stroke="var(--blue)" stroke-width="2.2"/><path d="M14 16l4 4 8-8" fill="none" stroke="var(--blue)" stroke-width="2.2"/></svg>Secure Online Payment</div>
    <p class="trust-text">Edce euismod consequat ante.<br>Lorem ipsum dolor sit amet,<br>consectetuer adipiscing elit.<br>Pellentesque sed dolor.</p>
    <p class="readmore">Readmore</p>
  </div>
</section>

<section class="app">
  <svg class="app-icon" width="40" height="66" viewBox="0 0 40 66"><rect x="2" y="2" width="36" height="62" rx="5" fill="none" stroke="var(--blue)" stroke-width="3"/><path d="M2 12h36M2 52h36" stroke="var(--blue)" stroke-width="2"/><circle cx="20" cy="58" r="2.5" fill="var(--blue)"/></svg>
  <h2 class="app-title">Get the Rinsora App</h2>
  <p class="app-sub">For phones and tablets. Download today.</p>
  <div class="stores"><div class="store-badge" aria-label="App store badge"></div><div class="store-badge" aria-label="App store badge"></div></div>
</section>

<footer class="site-footer">
  <div class="foot-brand abs">
    <div class="brand-name">Washvane.com</div>
    <div class="brand-tag">Fresh Folds, Next Day</div>
  </div>
  <div class="social abs"><span>Brookly</span><span>Chirpa</span><span>Plexo</span></div>
  <div class="foot-col abs" style="left:498px">
    <div class="foot-heading">Sitemap</div>
    <ul class="foot-links">
      <li>Home</li><li>Schedule a pickup</li><li>Pricing</li><li>Blog</li><li>Service Area</li><li>Commercial</li><li>Contact</li>
    </ul>
  </div>
  <div class="foot-col abs" style="left:805px">
    <div class="foot-heading">Quality Assurance:</div>
    <p class="qa-text">Every piece of laundry is handle with care by our trained attendants, we guarantee our service by double checking you wont have any missing clothes before delivery</p>
    <div class="seal"></div>
    <div class="cards"><div class="card-chip">Orbix</div><div class="card-chip">Veltra</div><div class="card-chip">Nuvia</div></div>
  </div>
</footer>

<div class="copyright abs">© 2015 washvane.com ,  All rights reserved.</div>

</body>
</html>
```